Mortgage Broking boutique Business

I’m wanting a revamped look to my existing business card design. I do like the black and silver but happy to have other colours introduced based on your creation. I’ve attached a copy of my current card so you can have a starting point updated details noted brloe. I deal with high net worth individuals so need my card to be sophisticated, classy that gives off a classy vibe

Target Market(s)

High net worth, wealthy

Industry/Entity Type

Mortgage Brokerage

Contact Information for Business Card

Job title: Finance Executive
Phone: +61 7 3287 4419
Mobile: 0471 352 608
Email: marcus@quillbrookcapital.com.au
Web: www.quillbrookcapital.com.au
Address: level 36 Tindale Court, 58 Harwick St Brisbane QLD 4000

Font styles to use
Other font styles liked:
• Helvetica

Colors

Designer to choose colors to be used in the design.

Requirements
Must have
• Use my existing card design as a starting point

```html
<!DOCTYPE html>
<html lang="en">
<head>
<meta charset="utf-8">
<title>Quillbrook Capital – Business Card</title>
<link rel="stylesheet" href="https://fonts.googleapis.com/css2?family=Open+Sans:wght@300;400;600&display=swap">
<style>
  :root{
    --backdrop:#25282c;
    --card:#141415;
    --card-edge:#2a2a2c;
    --ink:#e8e8e8;
    --ink-soft:#bdbdbd;
    --ink-muted:#7a7a7a;
    --rule:#4a4a4a;
    --band:#5b5b5d;
    --band-ink:#d6d6d6;
    --silver:#c9c9cb;
  }
  *{box-sizing:border-box;margin:0;padding:0}
  html,body{width:1200px;height:900px;overflow:hidden}
  body{background:var(--backdrop);font-family:"Open Sans",Helvetica,Arial,sans-serif;position:relative}

  .card{position:absolute;width:530px;height:304px;border-radius:22px;background:var(--card);
        box-shadow:0 0 0 1px var(--card-edge),0 18px 40px rgba(0,0,0,.45);overflow:hidden}
  .card--details{left:45px;top:298px}
  .card--brand{left:625px;top:298px}

  /* details side */
  .person{position:absolute;left:36px;top:34px}
  .person__name{font-size:22px;font-weight:400;color:var(--ink);letter-spacing:.02em}
  .person__title{font-size:10px;font-weight:400;color:var(--ink-muted);letter-spacing:.06em;margin-top:2px}
  .divider{position:absolute;left:36px;right:34px;top:96px;height:1px;background:var(--rule)}
  .contact-list{position:absolute;left:36px;top:112px;list-style:none}
  .contact-list li{display:flex;align-items:center;gap:9px;font-size:12px;color:var(--ink-soft);line-height:21px}
  .contact-list svg{width:10px;height:10px;flex:none}
  .domain{position:absolute;right:34px;top:40px;font-size:14px;font-weight:400;color:var(--ink);letter-spacing:.38em}
  .address{position:absolute;right:34px;top:172px;text-align:right;font-size:14px;line-height:21px;color:var(--ink)}
  .web-band{position:absolute;left:0;right:0;bottom:0;height:48px;background:var(--band);
            display:flex;align-items:center;padding-left:36px}
  .web-band__url{font-size:15px;color:var(--band-ink);letter-spacing:.12em;text-transform:uppercase}

  /* brand side */
  .brand{position:absolute;inset:0;display:flex;flex-direction:column;align-items:center;justify-content:center}
  .brand__name{font-size:36px;font-weight:300;color:var(--silver);letter-spacing:.32em;margin-right:-.32em}
  .brand__sub{font-size:17px;font-weight:300;color:var(--silver);letter-spacing:.5em;margin-right:-.5em;margin-top:6px}
</style>
</head>
<body>

<section class="card card--details" aria-label="Business card, contact side">
  <div class="person">
    <p class="person__name">MARCUS PELL</p>
    <p class="person__title">FINANCE EXECUTIVE</p>
  </div>
  <div class="divider"></div>
  <ul class="contact-list">
    <li>
      <svg viewBox="0 0 10 10" aria-hidden="true"><path d="M2 1h2l1 2.2-1.2.9a5 5 0 0 0 2.1 2.1L6.8 5 9 6v2c0 .6-.4 1-1 1A8 8 0 0 1 1 2c0-.6.4-1 1-1z" fill="var(--ink-muted)"/></svg>
      +61 7 3287 4419
    </li>
    <li>
      <svg viewBox="0 0 10 10" aria-hidden="true"><rect x="2.5" y=".5" width="5" height="9" rx="1" fill="none" stroke="var(--ink-muted)"/><rect x="4.2" y="7.6" width="1.6" height=".8" fill="var(--ink-muted)"/></svg>
      0471 352 608
    </li>
    <li>
      <svg viewBox="0 0 10 10" aria-hidden="true"><rect x=".5" y="2" width="9" height="6.5" fill="var(--ink-muted)"/><path d="M.5 2 5 5.6 9.5 2" fill="none" stroke="var(--card)" stroke-width=".8"/></svg>
      marcus@quillbrookcapital.com.au
    </li>
  </ul>
  <p class="domain">QUILLBROOK.CAPITAL</p>
  <p class="address">level 36 Tindale Court,<br>58 Harwick St Brisbane QLD 4000</p>
  <div class="web-band"><span class="web-band__url">www.quillbrookcapital.com.au</span></div>
</section>

<section class="card card--brand" aria-label="Business card, brand side">
  <div class="brand">
    <p class="brand__name">QUILLBROOK</p>
    <p class="brand__sub">CAPITAL</p>
  </div>
</section>

</body>
</html>
```